Bold Plum

I am starting a sharpening service for knives, scissors, and garden tools. It's a sole proprietorship, so it's a small business. The business name is "Bolt Plum." A one or two-page website is fine. Ember Guild has created a logo for me. There should be pictures of the things I sharpen. There will also be a price list for sharpened items. My address is: 18392 Calloway Lane, Maple Hollow, CA 91307. Phone number is 661-555-0172

```html
<!DOCTYPE html>
<html lang="en">
<head>
<meta charset="utf-8">
<title>Bolt Plum – Knife &amp; Tool Sharpening Service</title>
<link href="https://fonts.googleapis.com/css2?family=Poppins:wght@400;500;600;700&display=swap" rel="stylesheet">
<style>
:root{
  --navy:#24375f;
  --navy-deep:#1b2b4d;
  --red:#cf2027;
  --ink:#1e1e1e;
  --muted:#555a66;
  --footer:#1e2234;
  --pink:#efb9b9;
  --white:#ffffff;
}
*{box-sizing:border-box;margin:0;padding:0}
html,body{width:1200px;height:4393px;overflow:hidden}
body{position:relative;background:var(--white);font-family:'Poppins',sans-serif;color:var(--ink)}
.abs{position:absolute}
.shapes{position:absolute;left:0;top:0;width:1200px;height:4393px}
.hero-photo{position:absolute;left:0;top:123px;width:1200px;height:670px;
  background:radial-gradient(ellipse at 72% 55%,#c7862b 0%,#6e4a22 28%,#2f2a27 60%,#1c1d22 100%)}
.topbar-text{font-size:12px;color:#fff}
.social-dot{width:14px;height:14px;border:1.6px solid #fff;border-radius:50%}
.logo{font-weight:700;font-size:36px;color:var(--navy);letter-spacing:0.2px}
.nav a{position:absolute;top:72px;font-size:13px;color:#333;text-decoration:none}
.nav a.active{color:var(--red)}
.btn{position:absolute;background:var(--red);color:#fff;font-size:11px;font-weight:600;
  display:flex;align-items:center;justify-content:center;text-transform:uppercase}
.hero-title{left:158px;top:304px;font-size:44px;font-weight:600;line-height:49px;color:#fff}
.hero-sub{left:160px;top:418px;font-size:14px;line-height:16px;color:#fff;letter-spacing:0.4px}
.arrow{width:14px;height:14px;border-left:2px solid #fff;border-bottom:2px solid #fff}
.section-title{position:absolute;left:0;width:1200px;text-align:center;font-size:32px;font-weight:600}
.about-text{left:262px;top:880px;width:676px;text-align:center;font-size:12.5px;line-height:19.6px;color:#333}
.tri-title{position:absolute;width:240px;text-align:center;font-size:15px;font-weight:500;letter-spacing:0.8px;color:#222}
.tri-text{position:absolute;width:210px;text-align:center;font-size:11px;line-height:14px;color:#555}
.price-item .name{position:absolute;left:709px;font-size:15px;font-weight:500;color:#111}
.price-item .desc{position:absolute;left:709px;width:256px;font-size:12.5px;line-height:19px;color:#333}
.price-item .tag{position:absolute;left:1002px;font-size:14px;line-height:19px;color:#333}
.photo{position:absolute;width:194px;height:193px}
.card{left:162px;top:3573px;width:876px;height:515px;background:#fff;box-shadow:0 4px 24px rgba(0,0,0,0.12)}
.field{position:absolute;border:1px solid #c9c9c9;font-size:12.5px;color:#666;padding:18px 16px 0}
.footer-nav a{position:absolute;top:4222px;font-size:13px;color:#fff;text-decoration:none}
.contact-line{position:absolute;font-size:13px;line-height:15px;color:#fff}
.icon-circle{position:absolute;width:26px;height:26px;border-radius:50%;background:#fff}
</style>
</head>
<body>

<div class="hero-photo" role="img" aria-label="Worker grinding metal with an angle grinder, sparks flying"></div>

<svg class="shapes" viewBox="0 0 1200 4393" aria-hidden="true">
  <polygon points="384,0 1200,0 1200,37 350,37" fill="#23355a"/>
  <polygon points="0,752 598,640 1200,752 1200,795 0,795" fill="var(--red)"/>
  <polygon points="0,787 598,668 1200,787 1200,1080 0,1080" fill="#fff"/>
  <rect x="0" y="1070" width="1200" height="905" fill="var(--navy)"/>
  <rect x="0" y="1070" width="1200" height="905" fill="url(#sparkGlow)"/>
  <polygon points="0,1066 1200,1066 1200,1076 325,1196 0,1076" fill="#fff"/>
  <polygon points="0,1076 325,1196 1200,1076 1200,1090 325,1210 0,1102" fill="var(--red)"/>
  <polygon points="0,1950 895,1832 1200,1945 1200,1978 0,1978" fill="#fff"/>
  <polygon points="0,1940 895,1822 1200,1928 1200,1962 895,1834 0,1952" fill="var(--red)"/>
  <polygon points="382,1364 559,1659 205,1659" fill="#fff"/>
  <polygon points="426,1364 779,1364 602,1659" fill="#fff"/>
  <polygon points="818,1364 995,1659 641,1659" fill="#fff"/>
  <polygon points="293,2028 440,2548 0,2440 0,2380" fill="var(--pink)"/>
  <g role="img" aria-label="Hand sharpening a blade on a bench grinder">
    <polygon points="235,2020 372,2497 0,2408 0,2200" fill="url(#grinder)"/>
  </g>
  <g fill="var(--navy)">
    <polygon points="658,2130 690,2186 626,2186"/>
    <polygon points="658,2236 690,2292 626,2292"/>
    <polygon points="658,2342 690,2398 626,2398"/>
  </g>
  <g stroke="#fff" stroke-width="2.5" fill="none" stroke-linecap="round">
    <line x1="658" y1="2152" x2="658" y2="2178"/>
    <line x1="650" y1="2280" x2="668" y2="2258"/><circle cx="648" cy="2282" r="3"/>
    <line x1="650" y1="2386" x2="667" y2="2364"/><line x1="650" y1="2364" x2="667" y2="2386"/>
  </g>
  <rect x="0" y="2518" width="1200" height="965" fill="var(--navy)"/>
  <polygon points="0,2514 1200,2514 1200,2523 325,2651 0,2523" fill="#fff"/>
  <polygon points="0,2523 325,2651 1200,2523 1200,2537 325,2665 0,2549" fill="var(--red)"/>
  <polygon points="0,3458 895,3346 1200,3478 1200,3486 0,3486" fill="#fff"/>
  <polygon points="0,3442 895,3330 1200,3456 1200,3478 895,3346 0,3458" fill="var(--red)"/>
  <polygon points="0,3737 600,3880 1200,3737 1200,3760 600,3902 0,3765" fill="var(--red)"/>
  <polygon points="0,3765 600,3902 1200,3760 1200,4393 0,4393" fill="var(--footer)"/>
  <line x1="162" y1="4331" x2="1038" y2="4331" stroke="#3a3f55" stroke-width="1"/>
  <defs>
    <radialGradient id="sparkGlow" cx="0.8" cy="0.4" r="0.6">
      <stop offset="0" stop-color="#3d4e74"/>
      <stop offset="1" stop-color="#24375f" stop-opacity="0"/>
    </radialGradient>
    <linearGradient id="grinder" x1="0" y1="0" x2="1" y2="1">
      <stop offset="0" stop-color="#a9b4b8"/>
      <stop offset="0.45" stop-color="#2f8c8c"/>
      <stop offset="1" stop-color="#6c6f74"/>
    </linearGradient>
  </defs>
</svg>

<div class="abs social-dot" style="left:454px;top:12px"></div>
<div class="abs social-dot" style="left:493px;top:12px"></div>
<div class="abs social-dot" style="left:532px;top:12px"></div>
<svg class="abs" style="left:743px;top:12px" width="13" height="13" viewBox="0 0 24 24" aria-hidden="true"><path fill="#fff" d="M6.6 10.8a15.1 15.1 0 0 0 6.6 6.6l2.2-2.2a1 1 0 0 1 1-.25 11.4 11.4 0 0 0 3.6.57 1 1 0 0 1 1 1V20a1 1 0 0 1-1 1A17 17 0 0 1 3 4a1 1 0 0 1 1-1h3.5a1 1 0 0 1 1 1c0 1.25.2 2.450.57 3.57a1 1 0 0 1-.25 1z"/></svg>
<div class="abs topbar-text" style="left:765px;top:11px">661-555-0172</div>
<svg class="abs" style="left:865px;top:14px" width="14" height="10" viewBox="0 0 14 10" aria-hidden="true"><rect width="14" height="10" fill="#fff"/><path d="M0 0 7 6 14 0" fill="none" stroke="#23355a" stroke-width="1.4"/></svg>
<div class="abs topbar-text" style="left:891px;top:11px">hello@boltplum.example</div>

<div class="abs logo" style="left:160px;top:34px">Bolt Plum</div>
<nav class="nav">
  <a class="active" style="left:418px">Home</a>
  <a style="left:493px">About Us</a>
  <a style="left:590px">Services</a>
  <a style="left:682px">Price</a>
  <a style="left:750px">Gallery</a>
  <a style="left:827px">Contact Us</a>
</nav>
<div class="btn" style="left:917px;top:60px;width:121px;height:42px">Call Now</div>

<h1 class="abs hero-title">Bolt Plum - Knife &amp; Tool<br>Sharpening Service</h1>
<p class="abs hero-sub">Professional Sharpening for Knives, scissors, and garden tools,<br>Fast Affordable, Local.</p>
<div class="btn" style="left:160px;top:470px;width:137px;height:36px">Learn More</div>
<div class="abs arrow" style="left:32px;top:404px;transform:rotate(45deg)"></div>
<div class="abs arrow" style="left:1155px;top:404px;transform:rotate(-135deg)"></div>
<div class="abs" style="left:572px;top:613px;width:52px;height:52px;border-radius:50%;background:#fff;box-shadow:0 3px 10px rgba(0,0,0,0.3);display:flex;align-items:center;justify-content:center">
  <svg width="22" height="18" viewBox="0 0 22 18" aria-hidden="true"><path d="M2 2h18L11 16z M6 6h10" fill="none" stroke="var(--navy)" stroke-width="1.8" stroke-linejoin="round"/></svg>
</div>

<h2 class="section-title" style="top:824px">ABOUT US</h2>
<p class="abs about-text">Lorem Ipsum is simply dummy text of the printing and typesetting industry. Lorem Ipsum has been the industry's standard dummy text ever since the 1500s, when an unknown printer took a galley of type and scrambled it to make a type specimen book. It has survived not only five centuries, but also the leap into electronic typesetting, remaining essentially unchanged. It was popularised in the 1960s with the release of Letraset sheets containing Lorem Ipsum passages, and more recently with desktop publishing software like Aldus PageMaker including versions of Lorem Ipsum.</p>

<h2 class="section-title" style="top:1272px;color:#fff">OUR SERVICES</h2>
<svg class="abs" style="left:348px;top:1446px" width="70" height="70" viewBox="0 0 70 70" aria-hidden="true">
  <path d="M6 4 C24 20 44 38 60 52 L52 60 C36 44 20 26 6 4z" fill="var(--red)"/>
  <rect x="50" y="50" width="18" height="8" transform="rotate(45 59 54)" fill="#9a1519"/>
</svg>
<div class="tri-title" style="left:262px;top:1529px">KNIVES</div>
<div class="tri-text" style="left:277px;top:1556px">It is a long established fact that a reader will be distracted by th looking at its layout.</div>

<div class="tri-title" style="left:482px;top:1403px">SCISSORS</div>
<div class="tri-text" style="left:497px;top:1436px">It is a long established fact that a reader will be distracted by th looking at its layout.</div>
<svg class="abs" style="left:567px;top:1518px" width="74" height="74" viewBox="0 0 74 74" aria-hidden="true">
  <g fill="none" stroke="var(--red)" stroke-width="5"><circle cx="14" cy="50" r="8"/><circle cx="26" cy="62" r="8"/></g>
  <path d="M20 46 L70 6 L28 54z M30 56 L66 20 L24 44z" fill="var(--red)"/>
</svg>

<svg class="abs" style="left:780px;top:1440px" width="80" height="76" viewBox="0 0 80 76" aria-hidden="true">
  <path d="M8 4 L40 34 L34 40 Z M58 2 L38 30 L46 38 Z" fill="var(--red)"/>
  <path d="M40 36 L74 70 L66 74 L36 42 Z M38 40 L22 74 L14 70 L32 36 Z" fill="var(--red)"/>
  <circle cx="39" cy="37" r="3" fill="#fff"/>
</svg>
<div class="tri-title" style="left:698px;top:1529px">GARDEN TOOLS</div>
<div class="tri-text" style="left:713px;top:1556px">It is a long established fact that a reader will be distracted by th looking at its layout.</div>
<div class="btn" style="left:515px;top:1722px;width:170px;height:35px">Call Now</div>

<h2 class="abs" style="left:622px;top:2050px;font-size:32px;font-weight:600">SHARPENING PRICES</h2>
<div class="price-item">
  <div class="name" style="top:2124px">KITCHEN KNIVES</div>
  <div class="desc" style="top:2150px">Lorem Ipsum is simply dummy text of the printing and typesetting industry.</div>
  <div class="tag" style="top:2150px">Price<br>$50</div>
</div>
<div class="price-item">
  <div class="name" style="top:2230px">SCISSORS &amp; CLIPPERS</div>
  <div class="desc" style="top:2256px">Lorem Ipsum is simply dummy text of the printing and typesetting industry.</div>
  <div class="tag" style="top:2256px">Price<br>$50</div>
</div>
<div class="price-item">
  <div class="name" style="top:2336px">GARDEN TOOLS</div>
  <div class="desc" style="top:2362px">Lorem Ipsum is simply dummy text of the printing and typesetting industry.</div>
  <div class="tag" style="top:2362px">Price<br>$50</div>
</div>

<h2 class="section-title" style="top:2712px;color:#fff">OUR GALLERY</h2>
<div class="photo" style="left:184px;top:2806px;background:linear-gradient(135deg,#8b8f94,#c9a27c 55%,#4a4c52)" role="img" aria-label="Blade held against a grinding wheel"></div>
<div class="photo" style="left:397px;top:2806px;background:linear-gradient(135deg,#d99b4a,#a76a36 50%,#2a3145)" role="img" aria-label="Sparks flying from a sharpening wheel"></div>
<div class="photo" style="left:610px;top:2806px;background:linear-gradient(135deg,#5a5148,#c98a3d 55%,#2d2823)" role="img" aria-label="Angle grinder cutting metal with sparks"></div>
<div class="photo" style="left:822px;top:2806px;background:linear-gradient(135deg,#2f2b28,#b5683a 55%,#1f1c1a)" role="img" aria-label="Knife edge being ground on a bench grinder"></div>
<div class="photo" style="left:184px;top:3016px;background:linear-gradient(135deg,#c9a48d,#d8d9dc 55%,#8d9096)" role="img" aria-label="Hands honing a knife on a whetstone"></div>
<div class="photo" style="left:397px;top:3016px;background:linear-gradient(135deg,#7c6a5e,#4b4541 50%,#c77d3a)" role="img" aria-label="Hand pressing a blade to a grinder"></div>
<div class="photo" style="left:610px;top:3016px;background:linear-gradient(135deg,#3a3d41,#a9abae 55%,#b7342c)" role="img" aria-label="Gloved hand sharpening pruning shears with a file"></div>
<div class="photo" style="left:822px;top:3016px;background:linear-gradient(135deg,#b06a4f,#8f9397 50%,#5e8b3c)" role="img" aria-label="Garden pruning shears held outdoors"></div>
<div class="btn" style="left:515px;top:3268px;width:170px;height:35px">Call Now</div>

<div class="abs card">
  <h2 style="position:absolute;left:0;top:50px;width:876px;text-align:center;font-size:32px;font-weight:600">CONTACT US</h2>
  <div class="field" style="left:53px;top:131px;width:373px;height:50px">First Name</div>
  <div class="field" style="left:447px;top:131px;width:373px;height:50px">Last Name</div>
  <div class="field" style="left:53px;top:199px;width:373px;height:50px">Email Address</div>
  <div class="field" style="left:447px;top:199px;width:373px;height:50px">Phone Number</div>
  <div class="field" style="left:53px;top:267px;width:767px;height:149px">Message</div>
  <div class="btn" style="left:353px;top:450px;width:170px;height:35px">Submit</div>
</div>

<div class="abs logo" style="left:0;top:4134px;width:1200px;text-align:center;color:#fff">Bolt Plum</div>
<nav class="footer-nav">
  <a style="left:367px">About Us</a>
  <a style="left:478px">Services</a>
  <a style="left:585px">Price</a>
  <a style="left:669px">Gallery</a>
  <a style="left:760px">Contact Us</a>
</nav>
<div class="icon-circle" style="left:248px;top:4272px"></div>
<svg class="abs" style="left:254px;top:4278px" width="14" height="14" viewBox="0 0 24 24" aria-hidden="true"><path fill="var(--footer)" d="M6.6 10.8a15.1 15.1 0 0 0 6.6 6.6l2.2-2.2a1 1 0 0 1 1-.25 11.4 11.4 0 0 0 3.6.57 1 1 0 0 1 1 1V20a1 1 0 0 1-1 1A17 17 0 0 1 3 4a1 1 0 0 1 1-1h3.5a1 1 0 0 1 1 1c0 1.25.2 2.45.57 3.57a1 1 0 0 1-.25 1z"/></svg>
<div class="contact-line" style="left:285px;top:4278px">661-555-0172</div>
<div class="icon-circle" style="left:485px;top:4272px"></div>
<svg class="abs" style="left:491px;top:4280px" width="14" height="10" viewBox="0 0 14 10" aria-hidden="true"><rect width="14" height="10" fill="var(--footer)"/><path d="M0 0 7 6 14 0" fill="none" stroke="#fff" stroke-width="1.4"/></svg>
<div class="contact-line" style="left:522px;top:4276px">hello@boltplum.example</div>
<div class="icon-circle" style="left:764px;top:4272px"></div>
<svg class="abs" style="left:771px;top:4277px" width="12" height="16" viewBox="0 0 12 16" aria-hidden="true"><path d="M6 0a6 6 0 0 1 6 6c0 4-6 10-6 10S0 10 0 6a6 6 0 0 1 6-6z" fill="var(--footer)"/><circle cx="6" cy="6" r="2.2" fill="#fff"/></svg>
<div class="contact-line" style="left:801px;top:4271px">18392 Calloway Lane, Maple<br>Hollow, CA 91307</div>
<div class="abs social-dot" style="left:549px;top:4357px"></div>
<div class="abs social-dot" style="left:591px;top:4357px"></div>
<div class="abs social-dot" style="left:634px;top:4357px"></div>

</body>
</html>
```